A Freight forwarding (transportation/shipping) company requires stationary designs

We need The following:
1. Letterhead
2. Letter Envelope
3. Business Card Design
4. A4 Paper Envelope
5. A4 Paper Folder (One that is 2xA4 foldable size which we can open in half and we can put a paper in between and has a lot for business card)
6. A5 Paper (To be used for notes taking)
a design for a freight forwarding company named KORVELA MIND INTERNATIONAL TRANSPORTATION.
(We are active in Sea Transportation, Truck transportation, and Air Transportation, (printed design in PDF is required with all open source files for editing - lamination accepted)
Playing around with the Logo is accepted,, Korvela Logo.png is the correct logo.
Example of folder, envelopes, and notepad attached
Address of the company is :
No 7, 4th Tarandil Gharbi, Neshat Lar Blvd,
Mashhad, IR
Tel : +98 51 37412958
Fax : +98 51 37490316
Website : www.korvela-example.com
Email : info@korvela-example.com

```html
<!DOCTYPE html>
<html lang="en">
<head>
<meta charset="utf-8">
<title>Korvela Mind – Business Card</title>
<link href="https://fonts.googleapis.com/css2?family=Arimo:wght@400;700&display=swap" rel="stylesheet">
<style>
  :root{
    --stage:#a3a3a3;
    --navy:#2a2f8c;
    --navy-deep:#1d216d;
    --navy-light:#37419a;
    --ink:#1a1a1a;
    --brand-blue:#262c8a;
    --paper:#f7f7f7;
    --paper-edge:#e6e6e8;
    --white:#ffffff;
  }
  *{box-sizing:border-box;margin:0;padding:0}
  html,body{width:1200px;height:720px;overflow:hidden}
  body{
    background:var(--stage);
    font-family:"Arimo",Arial,sans-serif;
    display:flex;align-items:center;justify-content:center;gap:50px;
  }
  .card{
    width:540px;height:310px;position:relative;overflow:hidden;
    box-shadow:0 6px 18px rgba(0,0,0,.28);
  }
  /* front */
  .card--front{
    background:linear-gradient(135deg,var(--white) 0%,var(--paper) 55%,var(--paper-edge) 100%);
    color:var(--ink);
  }
  .brand{
    position:absolute;left:42px;top:34px;
    display:flex;align-items:center;gap:12px;
  }
  .brand__dot{
    width:58px;height:58px;border-radius:50%;
    border:4px solid var(--brand-blue);flex:none;
  }
  .brand__name{
    color:var(--brand-blue);font-weight:700;font-size:15px;line-height:1.25;
    letter-spacing:.3px;
  }
  .person{
    position:absolute;right:40px;top:132px;text-align:right;
  }
  .person__name{color:var(--brand-blue);font-weight:700;font-size:22px}
  .person__role{font-size:16px;margin-top:3px;letter-spacing:.5px}
  .contact{
    position:absolute;left:42px;bottom:34px;font-size:14.5px;line-height:1.35;
  }
  .contact__row{display:flex;align-items:flex-start;gap:9px;margin-top:5px}
  .contact__row svg{width:14px;height:14px;flex:none;margin-top:2px;fill:var(--brand-blue)}
  .contact__cols{display:flex;gap:36px;align-items:flex-end}
  /* back */
  .card--back{
    background:linear-gradient(120deg,var(--navy-light) 0%,var(--navy) 45%,var(--navy-deep) 100%);
    color:var(--white);
    display:flex;flex-direction:column;align-items:center;justify-content:center;gap:20px;
  }
  .seal{
    width:150px;height:150px;border-radius:50%;background:var(--white);
    display:flex;align-items:center;justify-content:center;text-align:center;
    outline:2px solid rgba(255,255,255,.6);outline-offset:5px;
  }
  .seal__name{color:var(--brand-blue);font-weight:700;font-size:15px;line-height:1.3;padding:0 16px}
  .web{font-size:15px;letter-spacing:.3px}
  .web b{font-weight:700}
</style>
</head>
<body>

<section class="card card--front" aria-label="Business card front">
  <div class="brand">
    <span class="brand__dot"></span>
    <div class="brand__name">KORVELA MIND<br>INTERNATIONAL<br>TRANSPORTATION</div>
  </div>

  <div class="person">
    <div class="person__name">Dorian K. Vale</div>
    <div class="person__role">C.E.O</div>
  </div>

  <div class="contact">
    <div class="contact__row">
      <svg viewBox="0 0 24 24"><path d="M12 2a7 7 0 0 0-7 7c0 5 7 13 7 13s7-8 7-13a7 7 0 0 0-7-7zm0 9.5A2.5 2.5 0 1 1 12 6.5a2.5 2.5 0 0 1 0 5z"/></svg>
      <span>No 7, 4th Tarandil Gharbi,<br>Neshat Lar Blvd, Mashhad, IR</span>
    </div>
    <div class="contact__cols">
      <div>
        <div class="contact__row">
          <svg viewBox="0 0 24 24"><path d="M6.6 10.8a15 15 0 0 0 6.6 6.6l2.2-2.2a1 1 0 0 1 1-.25 11.4 11.4 0 0 0 3.6.57 1 1 0 0 1 1 1V20a1 1 0 0 1-1 1A17 17 0 0 1 3 4a1 1 0 0 1 1-1h3.5a1 1 0 0 1 1 1c0 1.25.2 2.45.57 3.57a1 1 0 0 1-.25 1z"/></svg>
          <span>+98 51 37412958</span>
        </div>
        <div class="contact__row">
          <svg viewBox="0 0 24 24"><path d="M6 3h9l3 3v4H6zM4 11h16a2 2 0 0 1 2 2v6h-4v2H6v-2H2v-6a2 2 0 0 1 2-2zm4 5v3h8v-3z"/></svg>
          <span>+98 51 37490316</span>
        </div>
      </div>
      <div>
        <div class="contact__row">
          <svg viewBox="0 0 24 24"><path d="M2 5h20v14H2zm2 2v.5l8 5 8-5V7z"/></svg>
          <span>info@korvela-example.com</span>
        </div>
        <div class="contact__row">
          <svg viewBox="0 0 24 24"><path d="M12 2a10 10 0 1 0 0 20 10 10 0 0 0 0-20zm6.9 6h-3a15 15 0 0 0-1.3-4A8 8 0 0 1 18.9 8zM12 4c.8 1.1 1.5 2.5 1.9 4h-3.8c.4-1.5 1.1-2.9 1.9-4zM4.3 14a8 8 0 0 1 0-4h3.4a16 16 0 0 0 0 4zm.8 2h3a15 15 0 0 0 1.3 4A8 8 0 0 1 5.1 16zm3-8h-3a8 8 0 0 1 4.3-4 15 15 0 0 0-1.3 4zM12 20c-.8-1.1-1.5-2.5-1.9-4h3.8c-.4 1.5-1.1 2.9-1.9 4zm2.3-6H9.7a14 14 0 0 1 0-4h4.6a14 14 0 0 1 0 4zm.3 6a15 15 0 0 0 1.3-4h3a8 8 0 0 1-4.3 4zm1.7-6a16 16 0 0 0 0-4h3.4a8 8 0 0 1 0 4z"/></svg>
          <span>www.korvela-example.com</span>
        </div>
      </div>
    </div>
  </div>
</section>

<section class="card card--back" aria-label="Business card back">
  <div class="seal">
    <span class="seal__name">KORVELA MIND INTERNATIONAL TRANSPORTATION</span>
  </div>
  <div class="web">www.<b>korvela</b>-example.com</div>
</section>

</body>
</html>
```